Unique business card design

We are looking for a design that reflects our unique social media and online marketing agency "Kelvora Media". We are a young agency with a focus on speakers, coaches and trainers. In other words, we support people who want to do good with their work and help other people live a happier, more successful and fulfilling life, reach as many people as possible with their work and thus have an influence. Our values are: sustainability, creating added value, individuality, proactivity. We want our clients to feel comfortable with us and that's why the relationship with them is very important to us. We want every customer to become a lifelong friend of the company. Most of our clients are premium coaches, meaning they are in the higher priced segment and expect seriousness, professionalism and quality. All of these things should reflect our business card as well. I look forward to feedback. Best regards, Dorian Whitcombe
Look and feel
Each slider illustrates characteristics of the customer's brand and the style your logo design should communicate.

```html
<!DOCTYPE html>
<html lang="en">
<head>
<meta charset="utf-8">
<title>Kelvora Media – Business Card</title>
<link rel="stylesheet" href="https://fonts.googleapis.com/css2?family=Open+Sans:wght@400;600;700&display=swap">
<style>
  :root {
    --backdrop: #3a3230;
    --card: #17181a;
    --card-edge: #222326;
    --blue: #1f7fd6;
    --blue-deep: #1a3f9e;
    --text: #f2f2f2;
    --muted: #a9abb0;
    --divider: #8a8c90;
    --ghost: #2c2d30;
  }
  * { margin: 0; padding: 0; box-sizing: border-box; }
  html, body { width: 1200px; height: 864px; overflow: hidden; }
  body {
    background: var(--backdrop);
    font-family: "Open Sans", Arial, sans-serif;
    color: var(--text);
    position: relative;
  }
  .card {
    position: absolute;
    top: 283px;
    width: 525px;
    height: 300px;
    background: var(--card);
    border: 1px solid var(--card-edge);
    box-shadow: 0 14px 30px rgba(0,0,0,.45);
    overflow: hidden;
  }
  .card--front { left: 50px; }
  .card--back { left: 625px; }

  .brand { position: absolute; display: flex; flex-direction: column; }
  .brand__row { display: flex; align-items: center; gap: 10px; }
  .brand__square { width: 40px; height: 40px; background: var(--blue-deep); flex: none; }
  .brand__name { font-size: 24px; font-weight: 600; letter-spacing: .3px; line-height: 1; white-space: nowrap; }
  .brand__tagline { font-size: 11.5px; letter-spacing: .8px; margin-top: 8px; color: var(--text); white-space: nowrap; }

  .card--front .brand { left: 50%; top: 95px; transform: translateX(-50%); align-items: center; }
  .card--front .brand__name, .card--front .brand__tagline { color: var(--ghost); }
  .social { position: absolute; left: 50%; top: 188px; transform: translateX(-50%); display: flex; gap: 8px; }
  .social__dot { width: 20px; height: 20px; border-radius: 50%; background: var(--ghost); }

  .card--back .brand { left: 34px; top: 112px; }
  .divider { position: absolute; left: 285px; top: 42px; width: 1px; height: 216px; background: var(--divider); }

  .contact { position: absolute; left: 306px; top: 62px; }
  .contact__name { color: var(--blue); font-weight: 700; font-size: 17px; letter-spacing: .5px; }
  .contact__role { color: var(--muted); font-size: 12px; letter-spacing: .8px; margin-bottom: 10px; }
  .contact__address { font-size: 13px; line-height: 1.35; margin-bottom: 6px; white-space: nowrap; }
  .contact__list { list-style: none; font-size: 13px; }
  .contact__list li { display: flex; align-items: center; gap: 9px; line-height: 1.6; white-space: nowrap; }
  .icon { width: 12px; height: 12px; fill: var(--blue); flex: none; }
</style>
</head>
<body>
  <section class="card card--front" aria-label="Card front">
    <div class="brand">
      <div class="brand__row">
        <span class="brand__square"></span>
        <span class="brand__name">Kelvora Media</span>
      </div>
      <span class="brand__tagline">Online Marketing Services</span>
    </div>
    <div class="social" aria-label="Social profiles">
      <span class="social__dot"></span><span class="social__dot"></span><span class="social__dot"></span><span class="social__dot"></span><span class="social__dot"></span>
    </div>
  </section>

  <section class="card card--back" aria-label="Card back">
    <div class="brand">
      <div class="brand__row">
        <span class="brand__square"></span>
        <span class="brand__name">Kelvora Media</span>
      </div>
      <span class="brand__tagline">Online Marketing Services</span>
    </div>
    <div class="divider"></div>
    <div class="contact">
      <p class="contact__name">MAREN OLSBY</p>
      <p class="contact__role">PRESIDENT</p>
      <p class="contact__address">2170 Harrow Lane<br>Elm Ridge, NY 11420</p>
      <ul class="contact__list">
        <li><svg class="icon" viewBox="0 0 12 12"><path d="M2.5 1h2l1 2.5-1.3 1a6 6 0 0 0 3.3 3.3l1-1.3L11 7.5v2A1.5 1.5 0 0 1 9.5 11 8.5 8.5 0 0 1 1 2.5 1.5 1.5 0 0 1 2.5 1z"/></svg>555 0142 7731</li>
        <li><svg class="icon" viewBox="0 0 12 12"><path d="M3.5 0h5a1 1 0 0 1 1 1v10a1 1 0 0 1-1 1h-5a1 1 0 0 1-1-1V1a1 1 0 0 1 1-1zm.5 1.5v7.5h4V1.5z"/></svg>555 0198 2264</li>
        <li><svg class="icon" viewBox="0 0 12 12"><path d="M3 0h5v3H3zM1 4h10v6H9v2H3v-2H1zm3 4v3h4V8z"/></svg>555 0167 4409</li>
        <li><svg class="icon" viewBox="0 0 12 12"><path d="M0 2h12v8H0zm1 1v.4l5 3.3 5-3.3V3z"/></svg>maren@kelvora.com</li>
        <li><svg class="icon" viewBox="0 0 12 12"><circle cx="6" cy="6" r="6"/></svg>www.kelvoramedia.com</li>
      </ul>
    </div>
  </section>
</body>
</html>
```